A2 Desk calendar/planner *landscape*

We need a promotional a2 desk calendar for our customers (examples attached). Basically a marketing item so that our business is always fresh in the customer's mind sitting at their desk. It needs to be a2 Landscape as it will be a 20-page tear-off pad. Including logos, possibly images, 2020/21 calendar years, a big section in middle for writing on like examples. Business details and possibly a list of our industries and products. I have lots of images, logos and any other information visit www.corvallflow.com.au to get an idea of what we do.
Industry/Entity Type
Hydraulic
Font styles to use
Colors
Designer to choose colors to be used in the design.
Requirements
Must have
- Buisness logo, 2020 and 2021 calander year boxes like examples attached, colour themebluje and white possiby to go with the our logo. website adress phone number info. australian holiday dates . slogan "Industry chosen hose and fittings provider"
Nice to have
- public holiday dates from ; https://www.dunmerelabour.example.gov.au/law-compliance/laws-regulations/public-holidays

```html
<!DOCTYPE html>
<html lang="en">
<head>
<meta charset="utf-8">
<title>Corvall Hose and Fittings – 2020/2021 Desk Planner</title>
<link rel="stylesheet" href="https://fonts.googleapis.com/css2?family=Montserrat:wght@600;700;800&family=Roboto+Condensed:wght@400;500;700&family=Open+Sans:ital,wght@1,400;1,600&display=swap">
<style>
  :root{
    --blue:#2e3f97;
    --yellow:#f4d12b;
    --ink:#111111;
    --paper:#ffffff;
    --card:#f6f6f8;
    --rule:#7a7a7a;
    --badge:#d8232a;
  }
  *{margin:0;padding:0;box-sizing:border-box}
  html,body{width:1200px;height:849px;overflow:hidden;background:var(--paper)}
  .planner{position:relative;width:1200px;height:849px;background:var(--paper);font-family:"Roboto Condensed",sans-serif;color:var(--ink)}

  /* photo slots */
  .photo{position:absolute;width:194px;height:128px}
  .photo--hydraulic{left:0;top:0;background:linear-gradient(135deg,#f2c21a,#b8892a 55%,#3b3b3b)}
  .photo--quarry{left:205px;top:0;background:linear-gradient(180deg,#bcd3e8 0,#d9e4ee 35%,#6a5a46 60%,#3e342a)}
  .photo--manifold{left:0;top:138px;background:linear-gradient(135deg,#a9b4c2,#5e6b7c 50%,#c84a2e)}
  .photo--factory{left:205px;top:138px;background:linear-gradient(135deg,#d7dde4,#f08a1c 55%,#4b5563)}
  .photo--tunnel{left:803px;top:0;background:linear-gradient(160deg,#6b4a1e,#c58a2c 50%,#2b2013)}
  .photo--engine{left:1006px;top:0;background:linear-gradient(135deg,#8d95a0,#3a3f47 55%,#c9ccd1)}
  .photo--winery{left:803px;top:138px;background:linear-gradient(180deg,#cfd6dc,#9aa4ad 55%,#b23a3a 85%,#8c9298)}
  .photo--wheat{left:1006px;top:138px;background:linear-gradient(180deg,#c9d3dc 0,#dfe4e6 22%,#c99a55 30%,#b07f3c)}

  /* year panels */
  .year{position:absolute;top:274px;width:398px;height:575px}
  .year--2020{left:0;background:var(--blue);color:var(--paper)}
  .year--2021{left:803px;width:397px;background:var(--yellow);color:var(--ink)}
  .year__title{position:absolute;top:22px;left:0;width:100%;text-align:center;font-family:"Montserrat",sans-serif;font-weight:800;font-size:50px;letter-spacing:-1px;line-height:1}

  .months{position:absolute;left:22px;top:98px;display:grid;grid-template-columns:repeat(3,109px);column-gap:15px;grid-template-rows:repeat(4,107.5px)}
  .month{height:107.5px;overflow:hidden}
  .month__name{height:19px;text-align:center;font-size:13px;font-weight:500;line-height:19px}
  .month__card{background:var(--card);border-radius:4px;overflow:hidden;color:var(--ink);height:82px}
  .weekdays{display:grid;grid-template-columns:repeat(7,1fr);background:var(--ink);color:var(--paper);font-size:4.4px;height:13px;line-height:13px;text-align:center;padding:0 3px;list-style:none}
  .days{display:grid;grid-template-columns:repeat(7,1fr);grid-auto-rows:10.8px;padding:3px 3px 2px;list-style:none;font-size:5.2px;font-style:italic;font-weight:500;text-align:center;line-height:10.8px;color:var(--ink)}
  .days li:first-child{grid-column-start:var(--start)}

  .tagline{position:absolute;left:0;bottom:12px;width:100%;text-align:center;font-size:15.5px;font-weight:500;letter-spacing:.2px}

  /* centre notes */
  .brand{position:absolute;left:457px;top:52px;display:flex;align-items:center;gap:10px}
  .brand__dot{width:44px;height:44px;border-radius:50%;background:var(--blue)}
  .brand__name{font-family:"Montserrat",sans-serif;font-weight:800;font-size:25px;color:var(--blue);line-height:1;letter-spacing:.5px;text-transform:uppercase}
  .about{position:absolute;left:424px;top:131px;width:352px;text-align:center;font-family:"Open Sans",sans-serif;font-style:italic;font-size:10px;line-height:12.8px;color:#222}
  .notes__title{position:absolute;left:399px;width:404px;top:216px;text-align:center;font-family:"Montserrat",sans-serif;font-weight:700;font-size:27px}
  .notes__lines{position:absolute;left:424px;top:280px;width:353px;list-style:none}
  .notes__lines li{height:42px;border-top:1px solid var(--rule)}
  .notes__lines li:last-child{height:1px}
  .slogan{position:absolute;left:399px;width:404px;top:752px;text-align:center;font-family:"Montserrat",sans-serif;font-weight:700;font-size:12px;color:var(--blue);letter-spacing:.2px}
  .phone{position:absolute;left:399px;width:404px;top:772px;text-align:center;font-family:"Montserrat",sans-serif;font-weight:600;font-size:12px;color:var(--ink)}
  .website{position:absolute;left:423px;top:814px;font-family:"Montserrat",sans-serif;font-weight:600;font-size:18.5px;line-height:1;color:var(--ink)}
  .badge{position:absolute;left:708px;top:802px;width:66px;height:30px}
</style>
</head>
<body>
<main class="planner">

  <div class="photo photo--hydraulic" role="img" aria-label="Photo of yellow hydraulic cylinder with hoses"></div>
  <div class="photo photo--quarry" role="img" aria-label="Photo of earthmoving machinery at a quarry"></div>
  <div class="photo photo--manifold" role="img" aria-label="Photo of industrial pipework and braided hoses"></div>
  <div class="photo photo--factory" role="img" aria-label="Photo of factory machinery with hose connections"></div>
  <div class="photo photo--tunnel" role="img" aria-label="Photo of underground mining tunnel conveyor"></div>
  <div class="photo photo--engine" role="img" aria-label="Photo of vehicle engine bay"></div>
  <div class="photo photo--winery" role="img" aria-label="Photo of stainless tanks with red transfer hoses"></div>
  <div class="photo photo--wheat" role="img" aria-label="Photo of road train crossing a wheat field"></div>

  <!-- 2020 -->
  <section class="year year--2020">
    <h2 class="year__title">2020</h2>
    <div class="months">
      <div class="month"><h3 class="month__name">January</h3><div class="month__card"><ul class="weekdays"><li>SUN</li><li>MON</li><li>TUE</li><li>WED</li><li>THU</li><li>FRI</li><li>SAT</li></ul><ol class="days" style="--start:4"><li>1</li><li>2</li><li>3</li><li>4</li><li>5</li><li>6</li><li>7</li><li>8</li><li>9</li><li>10</li><li>11</li><li>12</li><li>13</li><li>14</li><li>15</li><li>16</li><li>17</li><li>18</li><li>19</li><li>20</li><li>21</li><li>22</li><li>23</li><li>24</li><li>25</li><li>26</li><li>27</li><li>28</li><li>29</li><li>30</li><li>31</li></ol></div></div>
      <div class="month"><h3 class="month__name">February</h3><div class="month__card"><ul class="weekdays"><li>SUN</li><li>MON</li><li>TUE</li><li>WED</li><li>THU</li><li>FRI</li><li>SAT</li></ul><ol class="days" style="--start:7"><li>1</li><li>2</li><li>3</li><li>4</li><li>5</li><li>6</li><li>7</li><li>8</li><li>9</li><li>10</li><li>11</li><li>12</li><li>13</li><li>14</li><li>15</li><li>16</li><li>17</li><li>18</li><li>19</li><li>20</li><li>21</li><li>22</li><li>23</li><li>24</li><li>25</li><li>26</li><li>27</li><li>28</li><li>29</li></ol></div></div>
      <div class="month"><h3 class="month__name">March</h3><div class="month__card"><ul class="weekdays"><li>SUN</li><li>MON</li><li>TUE</li><li>WED</li><li>THU</li><li>FRI</li><li>SAT</li></ul><ol class="days" style="--start:1"><li>1</li><li>2</li><li>3</li><li>4</li><li>5</li><li>6</li><li>7</li><li>8</li><li>9</li><li>10</li><li>11</li><li>12</li><li>13</li><li>14</li><li>15</li><li>16</li><li>17</li><li>18</li><li>19</li><li>20</li><li>21</li><li>22</li><li>23</li><li>24</li><li>25</li><li>26</li><li>27</li><li>28</li><li>29</li><li>30</li><li>31</li></ol></div></div>
      <div class="month"><h3 class="month__name">April</h3><div class="month__card"><ul class="weekdays"><li>SUN</li><li>MON</li><li>TUE</li><li>WED</li><li>THU</li><li>FRI</li><li>SAT</li></ul><ol class="days" style="--start:4"><li>1</li><li>2</li><li>3</li><li>4</li><li>5</li><li>6</li><li>7</li><li>8</li><li>9</li><li>10</li><li>11</li><li>12</li><li>13</li><li>14</li><li>15</li><li>16</li><li>17</li><li>18</li><li>19</li><li>20</li><li>21</li><li>22</li><li>23</li><li>24</li><li>25</li><li>26</li><li>27</li><li>28</li><li>29</li><li>30</li></ol></div></div>
      <div class="month"><h3 class="month__name">May</h3><div class="month__card"><ul class="weekdays"><li>SUN</li><li>MON</li><li>TUE</li><li>WED</li><li>THU</li><li>FRI</li><li>SAT</li></ul><ol class="days" style="--start:6"><li>1</li><li>2</li><li>3</li><li>4</li><li>5</li><li>6</li><li>7</li><li>8</li><li>9</li><li>10</li><li>11</li><li>12</li><li>13</li><li>14</li><li>15</li><li>16</li><li>17</li><li>18</li><li>19</li><li>20</li><li>21</li><li>22</li><li>23</li><li>24</li><li>25</li><li>26</li><li>27</li><li>28</li><li>29</li><li>30</li><li>31</li></ol></div></div>
      <div class="month"><h3 class="month__name">June</h3><div class="month__card"><ul class="weekdays"><li>SUN</li><li>MON</li><li>TUE</li><li>WED</li><li>THU</li><li>FRI</li><li>SAT</li></ul><ol class="days" style="--start:2"><li>1</li><li>2</li><li>3</li><li>4</li><li>5</li><li>6</li><li>7</li><li>8</li><li>9</li><li>10</li><li>11</li><li>12</li><li>13</li><li>14</li><li>15</li><li>16</li><li>17</li><li>18</li><li>19</li><li>20</li><li>21</li><li>22</li><li>23</li><li>24</li><li>25</li><li>26</li><li>27</li><li>28</li><li>29</li><li>30</li></ol></div></div>
      <div class="month"><h3 class="month__name">July</h3><div class="month__card"><ul class="weekdays"><li>SUN</li><li>MON</li><li>TUE</li><li>WED</li><li>THU</li><li>FRI</li><li>SAT</li></ul><ol class="days" style="--start:4"><li>1</li><li>2</li><li>3</li><li>4</li><li>5</li><li>6</li><li>7</li><li>8</li><li>9</li><li>10</li><li>11</li><li>12</li><li>13</li><li>14</li><li>15</li><li>16</li><li>17</li><li>18</li><li>19</li><li>20</li><li>21</li><li>22</li><li>23</li><li>24</li><li>25</li><li>26</li><li>27</li><li>28</li><li>29</li><li>30</li><li>31</li></ol></div></div>
      <div class="month"><h3 class="month__name">August</h3><div class="month__card"><ul class="weekdays"><li>SUN</li><li>MON</li><li>TUE</li><li>WED</li><li>THU</li><li>FRI</li><li>SAT</li></ul><ol class="days" style="--start:7"><li>1</li><li>2</li><li>3</li><li>4</li><li>5</li><li>6</li><li>7</li><li>8</li><li>9</li><li>10</li><li>11</li><li>12</li><li>13</li><li>14</li><li>15</li><li>16</li><li>17</li><li>18</li><li>19</li><li>20</li><li>21</li><li>22</li><li>23</li><li>24</li><li>25</li><li>26</li><li>27</li><li>28</li><li>29</li><li>30</li><li>31</li></ol></div></div>
      <div class="month"><h3 class="month__name">September</h3><div class="month__card"><ul class="weekdays"><li>SUN</li><li>MON</li><li>TUE</li><li>WED</li><li>THU</li><li>FRI</li><li>SAT</li></ul><ol class="days" style="--start:3"><li>1</li><li>2</li><li>3</li><li>4</li><li>5</li><li>6</li><li>7</li><li>8</li><li>9</li><li>10</li><li>11</li><li>12</li><li>13</li><li>14</li><li>15</li><li>16</li><li>17</li><li>18</li><li>19</li><li>20</li><li>21</li><li>22</li><li>23</li><li>24</li><li>25</li><li>26</li><li>27</li><li>28</li><li>29</li><li>30</li></ol></div></div>
      <div class="month"><h3 class="month__name">October</h3><div class="month__card"><ul class="weekdays"><li>SUN</li><li>MON</li><li>TUE</li><li>WED</li><li>THU</li><li>FRI</li><li>SAT</li></ul><ol class="days" style="--start:5"><li>1</li><li>2</li><li>3</li><li>4</li><li>5</li><li>6</li><li>7</li><li>8</li><li>9</li><li>10</li><li>11</li><li>12</li><li>13</li><li>14</li><li>15</li><li>16</li><li>17</li><li>18</li><li>19</li><li>20</li><li>21</li><li>22</li><li>23</li><li>24</li><li>25</li><li>26</li><li>27</li><li>28</li><li>29</li><li>30</li><li>31</li></ol></div></div>
      <div class="month"><h3 class="month__name">November</h3><div class="month__card"><ul class="weekdays"><li>SUN</li><li>MON</li><li>TUE</li><li>WED</li><li>THU</li><li>FRI</li><li>SAT</li></ul><ol class="days" style="--start:1"><li>1</li><li>2</li><li>3</li><li>4</li><li>5</li><li>6</li><li>7</li><li>8</li><li>9</li><li>10</li><li>11</li><li>12</li><li>13</li><li>14</li><li>15</li><li>16</li><li>17</li><li>18</li><li>19</li><li>20</li><li>21</li><li>22</li><li>23</li><li>24</li><li>25</li><li>26</li><li>27</li><li>28</li><li>29</li><li>30</li></ol></div></div>
      <div class="month"><h3 class="month__name">December</h3><div class="month__card"><ul class="weekdays"><li>SUN</li><li>MON</li><li>TUE</li><li>WED</li><li>THU</li><li>FRI</li><li>SAT</li></ul><ol class="days" style="--start:3"><li>1</li><li>2</li><li>3</li><li>4</li><li>5</li><li>6</li><li>7</li><li>8</li><li>9</li><li>10</li><li>11</li><li>12</li><li>13</li><li>14</li><li>15</li><li>16</li><li>17</li><li>18</li><li>19</li><li>20</li><li>21</li><li>22</li><li>23</li><li>24</li><li>25</li><li>26</li><li>27</li><li>28</li><li>29</li><li>30</li><li>31</li></ol></div></div>
    </div>
    <p class="tagline">HOSES&nbsp; |&nbsp; FITTINGS&nbsp; |&nbsp; EQUIPMENT&nbsp; |&nbsp; AGRICULTURE</p>
  </section>

  <!-- notes -->
  <section class="notes">
    <div class="brand">
      <span class="brand__dot"></span>
      <span class="brand__name">Corvall Hose<br>&amp; Fittings</span>
    </div>
    <p class="about">Corvall Hose and Fittings is an independent Adelaide-based company, managed and operated by a father-son duo with over 20 years of hose and fitting experience. We are wholesalers, distributors and service providers of hydraulic and industrial hose and fittings.</p>
    <h1 class="notes__title">NOTES</h1>
    <ul class="notes__lines"><li></li><li></li><li></li><li></li><li></li><li></li><li></li><li></li><li></li><li></li><li></li><li></li></ul>
    <p class="slogan">Industry chosen hose and fittings provider</p>
    <p class="phone">Phone (08) 5550 1234</p>
    <p class="website">www.corvallflow.com.au</p>
    <svg class="badge" viewBox="0 0 66 30" aria-hidden="true"><rect x="0" y="0" width="30" height="26" rx="3" fill="var(--badge)"/></svg>
  </section>

  <!-- 2021 -->
  <section class="year year--2021">
    <h2 class="year__title">2021</h2>
    <div class="months">
      <div class="month"><h3 class="month__name">January</h3><div class="month__card"><ul class="weekdays"><li>SUN</li><li>MON</li><li>TUE</li><li>WED</li><li>THU</li><li>FRI</li><li>SAT</li></ul><ol class="days" style="--start:6"><li>1</li><li>2</li><li>3</li><li>4</li><li>5</li><li>6</li><li>7</li><li>8</li><li>9</li><li>10</li><li>11</li><li>12</li><li>13</li><li>14</li><li>15</li><li>16</li><li>17</li><li>18</li><li>19</li><li>20</li><li>21</li><li>22</li><li>23</li><li>24</li><li>25</li><li>26</li><li>27</li><li>28</li><li>29</li><li>30</li><li>31</li></ol></div></div>
      <div class="month"><h3 class="month__name">February</h3><div class="month__card"><ul class="weekdays"><li>SUN</li><li>MON</li><li>TUE</li><li>WED</li><li>THU</li><li>FRI</li><li>SAT</li></ul><ol class="days" style="--start:2"><li>1</li><li>2</li><li>3</li><li>4</li><li>5</li><li>6</li><li>7</li><li>8</li><li>9</li><li>10</li><li>11</li><li>12</li><li>13</li><li>14</li><li>15</li><li>16</li><li>17</li><li>18</li><li>19</li><li>20</li><li>21</li><li>22</li><li>23</li><li>24</li><li>25</li><li>26</li><li>27</li><li>28</li></ol></div></div>
      <div class="month"><h3 class="month__name">March</h3><div class="month__card"><ul class="weekdays"><li>SUN</li><li>MON</li><li>TUE</li><li>WED</li><li>THU</li><li>FRI</li><li>SAT</li></ul><ol class="days" style="--start:2"><li>1</li><li>2</li><li>3</li><li>4</li><li>5</li><li>6</li><li>7</li><li>8</li><li>9</li><li>10</li><li>11</li><li>12</li><li>13</li><li>14</li><li>15</li><li>16</li><li>17</li><li>18</li><li>19</li><li>20</li><li>21</li><li>22</li><li>23</li><li>24</li><li>25</li><li>26</li><li>27</li><li>28</li><li>29</li><li>30</li><li>31</li></ol></div></div>
      <div class="month"><h3 class="month__name">April</h3><div class="month__card"><ul class="weekdays"><li>SUN</li><li>MON</li><li>TUE</li><li>WED</li><li>THU</li><li>FRI</li><li>SAT</li></ul><ol class="days" style="--start:5"><li>1</li><li>2</li><li>3</li><li>4</li><li>5</li><li>6</li><li>7</li><li>8</li><li>9</li><li>10</li><li>11</li><li>12</li><li>13</li><li>14</li><li>15</li><li>16</li><li>17</li><li>18</li><li>19</li><li>20</li><li>21</li><li>22</li><li>23</li><li>24</li><li>25</li><li>26</li><li>27</li><li>28</li><li>29</li><li>30</li></ol></div></div>
      <div class="month"><h3 class="month__name">May</h3><div class="month__card"><ul class="weekdays"><li>SUN</li><li>MON</li><li>TUE</li><li>WED</li><li>THU</li><li>FRI</li><li>SAT</li></ul><ol class="days" style="--start:7"><li>1</li><li>2</li><li>3</li><li>4</li><li>5</li><li>6</li><li>7</li><li>8</li><li>9</li><li>10</li><li>11</li><li>12</li><li>13</li><li>14</li><li>15</li><li>16</li><li>17</li><li>18</li><li>19</li><li>20</li><li>21</li><li>22</li><li>23</li><li>24</li><li>25</li><li>26</li><li>27</li><li>28</li><li>29</li><li>30</li><li>31</li></ol></div></div>
      <div class="month"><h3 class="month__name">June</h3><div class="month__card"><ul class="weekdays"><li>SUN</li><li>MON</li><li>TUE</li><li>WED</li><li>THU</li><li>FRI</li><li>SAT</li></ul><ol class="days" style="--start:3"><li>1</li><li>2</li><li>3</li><li>4</li><li>5</li><li>6</li><li>7</li><li>8</li><li>9</li><li>10</li><li>11</li><li>12</li><li>13</li><li>14</li><li>15</li><li>16</li><li>17</li><li>18</li><li>19</li><li>20</li><li>21</li><li>22</li><li>23</li><li>24</li><li>25</li><li>26</li><li>27</li><li>28</li><li>29</li><li>30</li></ol></div></div>
      <div class="month"><h3 class="month__name">July</h3><div class="month__card"><ul class="weekdays"><li>SUN</li><li>MON</li><li>TUE</li><li>WED</li><li>THU</li><li>FRI</li><li>SAT</li></ul><ol class="days" style="--start:5"><li>1</li><li>2</li><li>3</li><li>4</li><li>5</li><li>6</li><li>7</li><li>8</li><li>9</li><li>10</li><li>11</li><li>12</li><li>13</li><li>14</li><li>15</li><li>16</li><li>17</li><li>18</li><li>19</li><li>20</li><li>21</li><li>22</li><li>23</li><li>24</li><li>25</li><li>26</li><li>27</li><li>28</li><li>29</li><li>30</li><li>31</li></ol></div></div>
      <div class="month"><h3 class="month__name">August</h3><div class="month__card"><ul class="weekdays"><li>SUN</li><li>MON</li><li>TUE</li><li>WED</li><li>THU</li><li>FRI</li><li>SAT</li></ul><ol class="days" style="--start:1"><li>1</li><li>2</li><li>3</li><li>4</li><li>5</li><li>6</li><li>7</li><li>8</li><li>9</li><li>10</li><li>11</li><li>12</li><li>13</li><li>14</li><li>15</li><li>16</li><li>17</li><li>18</li><li>19</li><li>20</li><li>21</li><li>22</li><li>23</li><li>24</li><li>25</li><li>26</li><li>27</li><li>28</li><li>29</li><li>30</li><li>31</li></ol></div></div>
      <div class="month"><h3 class="month__name">September</h3><div class="month__card"><ul class="weekdays"><li>SUN</li><li>MON</li><li>TUE</li><li>WED</li><li>THU</li><li>FRI</li><li>SAT</li></ul><ol class="days" style="--start:4"><li>1</li><li>2</li><li>3</li><li>4</li><li>5</li><li>6</li><li>7</li><li>8</li><li>9</li><li>10</li><li>11</li><li>12</li><li>13</li><li>14</li><li>15</li><li>16</li><li>17</li><li>18</li><li>19</li><li>20</li><li>21</li><li>22</li><li>23</li><li>24</li><li>25</li><li>26</li><li>27</li><li>28</li><li>29</li><li>30</li></ol></div></div>
      <div class="month"><h3 class="month__name">October</h3><div class="month__card"><ul class="weekdays"><li>SUN</li><li>MON</li><li>TUE</li><li>WED</li><li>THU</li><li>FRI</li><li>SAT</li></ul><ol class="days" style="--start:6"><li>1</li><li>2</li><li>3</li><li>4</li><li>5</li><li>6</li><li>7</li><li>8</li><li>9</li><li>10</li><li>11</li><li>12</li><li>13</li><li>14</li><li>15</li><li>16</li><li>17</li><li>18</li><li>19</li><li>20</li><li>21</li><li>22</li><li>23</li><li>24</li><li>25</li><li>26</li><li>27</li><li>28</li><li>29</li><li>30</li><li>31</li></ol></div></div>
      <div class="month"><h3 class="month__name">November</h3><div class="month__card"><ul class="weekdays"><li>SUN</li><li>MON</li><li>TUE</li><li>WED</li><li>THU</li><li>FRI</li><li>SAT</li></ul><ol class="days" style="--start:2"><li>1</li><li>2</li><li>3</li><li>4</li><li>5</li><li>6</li><li>7</li><li>8</li><li>9</li><li>10</li><li>11</li><li>12</li><li>13</li><li>14</li><li>15</li><li>16</li><li>17</li><li>18</li><li>19</li><li>20</li><li>21</li><li>22</li><li>23</li><li>24</li><li>25</li><li>26</li><li>27</li><li>28</li><li>29</li><li>30</li></ol></div></div>
      <div class="month"><h3 class="month__name">December</h3><div class="month__card"><ul class="weekdays"><li>SUN</li><li>MON</li><li>TUE</li><li>WED</li><li>THU</li><li>FRI</li><li>SAT</li></ul><ol class="days" style="--start:4"><li>1</li><li>2</li><li>3</li><li>4</li><li>5</li><li>6</li><li>7</li><li>8</li><li>9</li><li>10</li><li>11</li><li>12</li><li>13</li><li>14</li><li>15</li><li>16</li><li>17</li><li>18</li><li>19</li><li>20</li><li>21</li><li>22</li><li>23</li><li>24</li><li>25</li><li>26</li><li>27</li><li>28</li><li>29</li><li>30</li><li>31</li></ol></div></div>
    </div>
    <p class="tagline">TRANSPORT&nbsp; |&nbsp; INDUSTRIALS&nbsp; |&nbsp; CONSTRUCTION&nbsp; |&nbsp; MINING</p>
  </section>

</main>
</body>
</html>
```